all sorted property services

Target Market(s)

General letter head for emails and letter quotes ect

Colors
0054AA
0677BA
7BADD7
CADEEF
E8F1F8
0094D4
00A9DD
6FCCEA
C7EBF8
E9F6FB

Requirements
Must have
• logo phone email website names
Nice to have
• what we do (from the website)

```html
<!DOCTYPE html>
<html lang="en">
<head>
<meta charset="utf-8">
<title>All Sorted Property Services – Letterhead</title>
<link href="https://fonts.googleapis.com/css2?family=Montserrat:wght@500;600;700&family=Open+Sans:wght@400;600&display=swap" rel="stylesheet">
<style>
  :root {
    --brand-deep: #0054AA;
    --brand-mid: #0677BA;
    --brand-bright: #0094D4;
    --brand-sky: #00A9DD;
    --navy: #233a7a;
    --navy-dark: #1f2467;
    --ink: #111111;
    --text-body: #8a8a8a;
    --text-dark: #3d3d3d;
    --rule: #dedede;
    --watermark: #f1f1f1;
    --page-bg: #ececed;
    --paper: #ffffff;
  }
  * { box-sizing: border-box; margin: 0; padding: 0; }
  html, body { width: 999px; height: 1200px; overflow: hidden; background: var(--page-bg); }
  .letterhead {
    position: absolute; left: 80px; top: 11px;
    width: 840px; height: 1178px;
    background: var(--paper);
    overflow: hidden;
    font-family: "Open Sans", sans-serif;
  }
  .brand {
    position: absolute; left: 74px; top: 72px;
    display: flex; align-items: center; gap: 12px;
  }
  .brand-dot { width: 46px; height: 46px; border-radius: 50%; background: var(--brand-mid); flex: none; }
  .brand-name {
    font-family: "Montserrat", sans-serif; font-weight: 700;
    color: var(--brand-deep); font-size: 20px; line-height: 1.1; letter-spacing: 0.3px;
    text-transform: uppercase;
  }
  .brand-name small { display: block; font-size: 10.5px; letter-spacing: 2.6px; }
  .contact-list {
    position: absolute; left: 596px; top: 62px; list-style: none;
    font-size: 11.5px; color: var(--text-dark); line-height: 1.25;
  }
  .contact-list li { display: flex; align-items: flex-start; gap: 7px; margin-bottom: 10px; }
  .contact-list svg { width: 15px; height: 15px; flex: none; }
  .header-rule { position: absolute; left: 60px; top: 218px; width: 718px; height: 2px; background: var(--rule); }
  .recipient { position: absolute; left: 77px; top: 318px; color: var(--text-dark); font-family: "Montserrat", sans-serif; font-weight: 500; font-size: 13.5px; line-height: 1.35; }
  .recipient-name { color: var(--navy); font-weight: 700; font-size: 21px; margin-bottom: 9px; }
  .recipient p { margin-bottom: 9px; }
  .letter-date { position: absolute; right: 74px; top: 428px; font-size: 16px; font-weight: 600; color: var(--text-dark); }
  .letter-body { position: absolute; left: 77px; top: 474px; width: 688px; color: var(--text-body); font-family: "Montserrat", sans-serif; font-weight: 500; font-size: 14.4px; line-height: 24.6px; text-align: justify; }
  .letter-body p + p { margin-top: 24.6px; }
  .sign-name { position: absolute; right: 73px; top: 828px; font-family: "Montserrat", sans-serif; font-weight: 600; font-size: 24px; color: var(--ink); }
  .signature { position: absolute; left: 612px; top: 872px; width: 128px; height: 86px; background: linear-gradient(90deg, #f4f4f4, #e9e9e9); }
  .watermark { position: absolute; left: 60px; top: 846px; width: 356px; height: 356px; border-radius: 50%; background: var(--watermark); }
  .footer-band { position: absolute; left: 0; bottom: 0; width: 840px; height: 16px; }
</style>
</head>
<body>
<main class="letterhead">
  <div class="watermark" aria-hidden="true"></div>

  <header>
    <div class="brand">
      <span class="brand-dot"></span>
      <div class="brand-name">All Sorted<small>Property Services</small></div>
    </div>
    <ul class="contact-list">
      <li><svg viewBox="0 0 16 16"><rect width="16" height="16" rx="3" fill="#233a7a"/><path d="M8 3.5a3 3 0 0 0-3 3c0 2.2 3 6 3 6s3-3.8 3-6a3 3 0 0 0-3-3z" fill="#fff"/><circle cx="8" cy="6.5" r="1.1" fill="#233a7a"/></svg><span>218 Harbor Lane<br>Easton, MD 21601</span></li>
      <li><svg viewBox="0 0 16 16"><rect width="16" height="16" rx="3" fill="#0094D4"/><path d="M5 3.8l1.6 2.1-1 1.1a6 6 0 0 0 3.4 3.4l1.1-1 2.1 1.6-1 1.6C7.6 12.5 3.5 8.4 3.4 4.8z" fill="#fff"/></svg><span>+1 410 555 0142</span></li>
      <li><svg viewBox="0 0 16 16"><rect width="16" height="16" rx="3" fill="#0094D4"/><rect x="3.5" y="5" width="9" height="6.5" rx="1" fill="none" stroke="#fff" stroke-width="1.2"/><path d="M3.8 5.5L8 8.6l4.2-3.1" fill="none" stroke="#fff" stroke-width="1.2"/></svg><span>hello@allsortedmail.com</span></li>
      <li><svg viewBox="0 0 16 16"><rect width="16" height="16" rx="3" fill="#0094D4"/><path d="M5 4l6.5 4-3 .6 1.7 3-1.2.7-1.7-3-2.3 2z" fill="#fff"/></svg><span>www.allsortedproperty.com</span></li>
    </ul>
    <div class="header-rule"></div>
  </header>

  <section class="recipient">
    <h2 class="recipient-name">MARA ELLISON</h2>
    <p>410-555-0187</p>
    <p>mara@ellisonmail.com</p>
    <p>77 Maple Court Suite 4<br>Dover, DE 19901</p>
  </section>

  <time class="letter-date">12 December, 2024</time>

  <article class="letter-body">
    <p>Lorem ipsum dolor sit amet, consectetuer adipiscing elit, sed diam nonummy nibh euismod tincidunt ut laoreet dolore magna aliquam erat volutpat. Ut wisi enim ad minim veniam, quis nostrud exerci tation ullamcorper suscipit lobortis nisl ut aliquip ex ea commodo consequat. Duis autem vel eum iriure dolor in hendrerit in vulputate velit esse molestie consequat, vel illum dolore eu feugiat nulla facilisis at vero eros et accumsan et iusto odio dignissim qui blandit praesent luptatum zzril delenit augue duis dolore te feugait nulla facilisi.</p>
    <p>Lorem ipsum dolor sit amet, cons ectetuer adipiscing elit, sed diam nonummy nibh euismod tincidunt ut laoreet dolore magna aliquam erat volutpat. Ut wisi enim ad minim veniam, quis nostrud exerci tation ullamcorper suscipit lobortis nisl ut aliquip ex ea commodo consequat.</p>
  </article>

  <div class="sign-name">Ms. Mara Ellison</div>
  <div class="signature" role="img" aria-label="Handwritten signature of Mara Ellison"></div>

  <svg class="footer-band" viewBox="0 0 840 16" preserveAspectRatio="none" aria-hidden="true">
    <defs>
      <linearGradient id="bandGradient" x1="0" x2="1" y1="0" y2="0">
        <stop offset="0" stop-color="#00A9DD"/>
        <stop offset="0.45" stop-color="#0677BA"/>
        <stop offset="1" stop-color="#1f2467"/>
      </linearGradient>
    </defs>
    <polygon points="330,0 840,0 840,16 300,16" fill="url(#bandGradient)"/>
  </svg>
</main>
</body>
</html>
```